Joan Pelley Letter Head

log and letter head

would like a modern feminine approch, please see attached the back of my business card

Joan Pelley Consulting

ABN 81 305 642 918

Address19a Brood Street Kestrel Bay 5072 South Australia

Business

```html
<!DOCTYPE html>
<html lang="en">
<head>
<meta charset="utf-8">
<title>Joan Pelley Consulting – Letterhead</title>
<link rel="stylesheet" href="https://fonts.googleapis.com/css2?family=Montserrat:wght@400;500&display=swap">
<style>
  :root {
    --backdrop: #e9e9e9;
    --paper: #f7f7f7;
    --brand-red: #c8142f;
    --on-red: #fbeaec;
  }
  * { margin: 0; padding: 0; box-sizing: border-box; }
  html, body {
    width: 1200px;
    height: 900px;
    overflow: hidden;
    background: var(--backdrop);
    font-family: "Montserrat", Arial, sans-serif;
  }
  .canvas {
    width: 1200px;
    height: 900px;
    display: flex;
    align-items: center;
    justify-content: center;
  }
  .letterhead {
    position: relative;
    width: 594px;
    height: 840px;
    background: var(--paper);
    box-shadow: 0 2px 10px rgba(0, 0, 0, 0.08);
  }
  .letterhead__band {
    height: 128px;
    background: var(--brand-red);
    display: flex;
    align-items: center;
    justify-content: center;
    padding-left: 60px;
  }
  .brand-name {
    color: var(--on-red);
    font-weight: 400;
    font-size: 22px;
    letter-spacing: 0.14em;
    text-transform: uppercase;
  }
  .letterhead__address {
    margin-top: 12px;
    padding-left: 160px;
    color: var(--brand-red);
    font-size: 9.5px;
    font-weight: 400;
    letter-spacing: 0.02em;
  }
  .letterhead__abn {
    position: absolute;
    right: 40px;
    bottom: 86px;
    color: var(--brand-red);
    font-size: 7px;
    font-weight: 400;
    letter-spacing: 0.03em;
  }
</style>
</head>
<body>
  <main class="canvas">
    <article class="letterhead">
      <header class="letterhead__band">
        <p class="brand-name">Joan Pelley Consulting</p>
      </header>
      <p class="letterhead__address">47c Tallow Street Kestrel Bay 5072 South Australia</p>
      <p class="letterhead__abn">ABN 81 305 642 918</p>
    </article>
  </main>
</body>
</html>
```